RQN Summit Services - Partnership Proposal

My company RQN is a study abroad consultant and We want to send a proposal to Universities and Educational institutions to partner with us. This proposal shall be used by our marketing team to collaborate with more than 100 top universities of the world and hence it must look like an extremely professional presentation.

Target Market(s)

Education institutions and Universities

Industry/Entity Type

Education

Font styles to use
Serif

Colors

Designer to choose colors to be used in the design.

Requirements
Must have
• A professional and neat look with company logo.
Nice to have
• Would like to see some the text presented in an interesting eye catchy manner.
Should not have
• Should not have too many colours or different fonts

```html
<!DOCTYPE html>
<html lang="en">
<head>
<meta charset="utf-8">
<title>RQN Summit Services – Partnership Proposal</title>
<link href="https://fonts.googleapis.com/css2?family=Arimo:ital,wght@0,400;0,700;1,700&family=Jost:wght@400&display=swap" rel="stylesheet">
<style>
  :root{
    --paper:#f0f1f1;
    --ink:#1f1f1f;
    --cyan:#3ee0dc;
    --cyan-text:#2fd6d2;
    --panel-dark:#1e1f22;
    --panel-mid:#3a3d40;
    --panel-light:#565b5f;
    --white:#ffffff;
  }
  *{margin:0;padding:0;box-sizing:border-box}
  html,body{width:1200px;height:849px;overflow:hidden;background:var(--paper)}
  body{font-family:"Arimo",Arial,sans-serif;color:var(--ink)}
  .page{position:relative;width:1200px;height:849px}
  .section-title{position:absolute;font-weight:700;font-style:italic;color:var(--cyan-text);text-transform:uppercase}
  .body-copy{position:absolute;font-size:13.4px;line-height:16.6px;text-align:justify}
  .body-copy p{text-indent:36px}
  .body-copy p + p{margin-top:16px}

  /* Background */
  .background-title{left:37px;top:36px;font-size:20px}
  .background-copy{left:37px;top:63px;width:531px}

  /* Why partner */
  .why{position:absolute;left:41px;top:351px;width:523px;height:333px;font-family:"Jost",sans-serif}
  .why-head{position:absolute;left:0;top:0;width:523px;height:40px;background:var(--cyan);color:var(--ink);font-size:31px;line-height:40px;padding-left:14px}
  .why-row{position:absolute;left:0;width:523px;font-size:24.5px;line-height:31px;text-align:center}
  .row-track{top:40px;height:87px;background:var(--panel-dark);color:var(--cyan);padding-top:13px}
  .row-convert{top:127px;height:111px;background:var(--panel-mid);color:var(--white);padding-top:17px}
  .row-team{top:238px;height:95px;background:var(--panel-light);color:var(--white);padding-top:17px}
  .why svg{position:absolute;left:0;top:0}

  /* Additional support */
  .support-title{left:41px;width:523px;top:706px;font-size:16px;text-align:center}
  .support-copy{position:absolute;left:41px;top:725px;width:523px;font-size:13.2px;line-height:16.8px;text-align:center}

  /* Approach */
  .approach-title{left:616px;top:13px;font-size:19.5px;color:var(--ink)}
  .approach-frame{position:absolute;left:616px;top:41px;width:580px;height:354px;background:var(--cyan)}
  .approach-panel{position:absolute;left:628px;top:56px;width:543px;height:327px;background:var(--panel-dark)}
  .approach-label{position:absolute;left:616px;top:41px;width:367px;height:36px;background:var(--cyan);font-size:12.6px;line-height:15.5px;padding:3px 0 0 8px}
  .reason{position:absolute;left:645px;width:515px;color:var(--white);font-size:12.4px;line-height:15.6px;text-indent:36px}
  .reason-one{top:91px}
  .reason-two{top:244px}
  .reason-three{top:336px}
  .tick{position:absolute;left:652px}

  /* Team */
  .team-title{left:620px;width:563px;top:406px;font-size:16px;text-align:center}
  .team-copy{left:620px;top:425px;width:563px;font-size:13.4px;line-height:17.2px}
  .team-copy p + p{margin-top:0}
  .member{color:var(--cyan-text)}
</style>
</head>
<body>
<main class="page">

  <h2 class="section-title background-title">Background</h2>
  <div class="body-copy background-copy">
    <p>RQN Summit Services Limited is a New Zealand based company established in 2013, engaged in providing end-to-end study abroad and migration services to international students and families. Headed by a Licensed Immigration Adviser with a strong social media presence and a sales &amp; service team operating from different parts of the world. RQN has been servicing clients from more than 30 countries of the world like India, Sri Lanka, Maldives, UAE, Egypt, Brazil, etc. The company boasts of being a specialist in New Zealand student enrollment and also offers after arrival support by an experienced and efficient onshore team.</p>
    <p>RQN is proud to have successfully served all the leading New Zealand Institutions. Having spent over a decade in this pursuit and realizing the ever increasing growth of study abroad aspirants, the core team of RQN is now keen to expand into other countries and set a global footprint in overseas education domain. Our consistent and creative social media marketing initiatives are attracting topnotch students from different countries to study in high quality global institutions.</p>
  </div>

  <section class="why">
    <div class="why-row row-track">○ Proven track record of student enrollment<br>for New Zealand</div>
    <div class="why-row row-convert">○ High conversion rate - application<br>to enrolment</div>
    <div class="why-row row-team">○ Qualified and experienced team<br>across countries</div>
    <div class="why-head">WHY PARTNER WITH US?</div>
    <svg width="523" height="333" aria-hidden="true">
      <polygon points="40,40 62,40 51,50" fill="var(--cyan)"/>
      <polygon points="40,227 62,227 51,237" fill="var(--panel-mid)"/>
    </svg>
  </section>

  <h2 class="section-title support-title">Additional support to our students</h2>
  <p class="support-copy">Our New Zealand success rides firmly on the onshore support we provide to our students once they arrive here. We aim to create the same model in your country as well as soon as active recruitment starts. We will be appointing an onshore adviser in your country who together with the your institution team will create a robust partnership between institution and agent to support our students.</p>

  <h2 class="section-title approach-title">Our approach and benefit to your institution</h2>
  <div class="approach-frame"></div>
  <div class="approach-panel"></div>
  <div class="approach-label">We are expanding beyond attracting students to New Zealand<br>due to the following reasons:</div>

  <svg class="tick" style="top:98px" width="12" height="10" aria-hidden="true"><polyline points="1,5 4,8 11,1" fill="none" stroke="var(--cyan)" stroke-width="2"/></svg>
  <p class="reason reason-one">The number of international students coming to New Zealand at both the high school and tertiary level is approximately 140,000 annually and increasing consistently. Some of them seek to move into institutions such as your institution after completion of their courses in New Zealand because they are either not able to get an admission into a New Zealand university since there are only 8 of them. Or they are simply keen to move into a larger country having experienced new Zealand (see results of a survey we conducted). There are limited agencies in New Zealand assisting in such a move and we aim to fill this gap in the market. This is our mutual opportunity to tap into a whole new segment of potential international students moving between countries.</p>

  <svg class="tick" style="top:251px" width="12" height="10" aria-hidden="true"><polyline points="1,5 4,8 11,1" fill="none" stroke="var(--cyan)" stroke-width="2"/></svg>
  <p class="reason reason-two">When we recruit students for New Zealand institutions from our main markets, most of them seek to have a 2nd option of a different country and an institution like your institution. Eventually a significant number choose not to go to New Zealand and we would like to offer them more options. This is the other reason we are embarking on this expansion and reaching out to you.</p>

  <svg class="tick" style="top:343px" width="12" height="10" aria-hidden="true"><polyline points="1,5 4,8 11,1" fill="none" stroke="var(--cyan)" stroke-width="2"/></svg>
  <p class="reason reason-three">Considering XYZ University has courses which can be very attractive to the above set of students, we will be delighted to partner with you. Bolstered by your exceptional student credentials and our professional focus we foresee a good partnership.</p>

  <h2 class="section-title team-title">The team and advisers</h2>
  <div class="body-copy team-copy">
    <p><span class="member">Daniel Marsh, Director -</span> He holds a Bachelor of Commerce with honors degree as well as a GCNZIA from Harbourview Polytechnic. He has a full license to practice as a Licensed Immigration Adviser and is based in Hamilton, New Zealand. He was a chairperson of Aotea Specialist Agents (ASA), the elite group of education agents formed under the aegis of Study Aotea Council. He was accorded the privilege of a private audience with His Excellency the Governor General of New Zealand in recognition of his services towards the promotion of New Zealand education.</p>
    <p><span class="member">Dr Elias Varenko -</span> Dr Varenko is a former Policy Officer with the New Zealand Department of Trade and Industry as well as New Zealand Ministry of Foreign Affairs and Trade. He was also a MBA lecturer in international trade and global enterprise. With this plethora of experience and knowledge he is an invaluable member of our advisory board and plays an important and active role in our future growth.</p>
    <p><span class="member">Helen Prescott -</span> With a background in teaching, academic and marketing roles Helen has a wealth of experience and knowledge to reflect on and actively mentor our future growth. She worked for 24 years in New Zealand Government tertiary institutions as a Lecturer, Head of Department, Business Liaison Manager, International Manager and International Marketing Manager. She has qualifications from Kauri Coast University and Ashbury University.</p>
    <p>Other team members based in India include 20 education advisers/counsellors and 6 visa processing staff and together they manage the entire student process from enquiry to a successful visa application. They are competent with the processes for all countries.</p>
  </div>

</main>
</body>
</html>
```